Marlow Lift Gates

we need a full webpage design thats modern, yet user friendly, we need our clients to be able to get a hold of us at a click of a button (chat or email)
Marlow lift gates is a garage door company
We are family owned and operated since 1965
We repair all garage doors, and do installations for commercial and residential
no job is too big or too small, were all about honesty and integrity, we take pride on our quality worksmanship. We have spanish speakers on site, weaccept allmajor credit cards, we have senior and military discounts.

Target Market(s)

All San Diego, not just Vista.

Industry/Entity Type

Garage

Font styles to use
Sans Serif

Colors
ffffff
0655a3
33a6d7
00a98f
edf7f6

Requirements
Must have
• we speak Spanish(hablamos espanol)
free estimates
contract license #524906
FAMILY owned and operated
in business since1965
accept all major credit cards
Nice to have
• lets add a jesus fish on there somewhere ;)
a little bit of flash
quick fill out form (name, number, service needed)
Use the word "affordable" somewhere

```html
<!DOCTYPE html>
<html lang="en">
<head>
<meta charset="utf-8">
<title>Marlow Lift Gates – Garage Door Repair & Installation</title>
<link href="https://fonts.googleapis.com/css2?family=Figtree:ital,wght@0,400;0,500;0,600;0,700;0,800;1,500;1,700&display=swap" rel="stylesheet">
<style>
:root{
  --white:#ffffff;
  --blue:#0655a3;
  --blue-deep:#043f7a;
  --sky:#33a6d7;
  --teal:#00a98f;
  --teal-deep:#00846f;
  --mist:#edf7f6;
  --ink:#1b1b1b;
  --body:#232323;
  --header:#1c1c1c;
  --muted:#b9b9b9;
}
*{margin:0;padding:0;box-sizing:border-box}
html,body{width:1024px;height:1200px;overflow:hidden;background:var(--body)}
body{font-family:"Figtree",sans-serif;color:var(--muted);position:relative}
.abs{position:absolute}

/* header */
.site-header{position:absolute;left:0;top:0;width:1024px;height:96px;background:linear-gradient(#2a2a2a 0,#2a2a2a 4px,var(--header) 4px)}
.brand{position:absolute;left:124px;top:18px;width:184px;height:62px;background:var(--ink);border:3px solid var(--sky);display:flex;align-items:center;justify-content:center;gap:7px}
.brand-mark{width:11px;height:11px;background:var(--sky);flex:none}
.brand-name{font-weight:800;font-size:17px;color:var(--white);line-height:1;white-space:nowrap}
.tagline{left:328px;top:32px;font-style:italic;font-weight:700;font-size:14px;line-height:15px;color:var(--white)}
.tagline .spanish{display:block;margin-top:6px;font-weight:500;color:#8d8d8d;letter-spacing:.5px}
.fish{left:604px;top:10px}
.callout{left:566px;top:32px;font-size:10px;letter-spacing:1px;color:#9a9a9a;display:flex;align-items:center;gap:5px}
.callout b{color:var(--sky)}
.head-phones{left:566px;top:51px;font-weight:700;font-size:14px;line-height:18px;color:#9a9a9a}
.head-phones span{color:var(--sky)}
.license{left:776px;top:4px;width:120px;height:20px;background:#3a3a3a;font-size:10px;color:#bdbdbd;text-align:center;line-height:20px;border-radius:0 0 3px 3px}
.quote-btn{left:776px;top:53px;width:118px;height:29px;background:linear-gradient(var(--teal),var(--teal-deep));border-radius:3px;color:var(--white);font-size:9.5px;font-weight:700;display:flex;align-items:center;justify-content:center;gap:5px;box-shadow:0 2px 0 #0d0d0d}

/* nav */
.main-nav{position:absolute;left:0;top:96px;width:1024px;height:42px;background:linear-gradient(var(--sky),var(--blue));border-top:1px solid #5cc0e8}
.main-nav a{position:absolute;top:0;height:41px;line-height:41px;text-align:center;font-weight:700;font-size:11.5px;color:var(--mist);text-decoration:none;border-left:1px solid var(--blue-deep);text-shadow:0 1px 0 var(--blue-deep)}
.main-nav a.active{background:var(--ink);color:var(--white);text-shadow:none}

/* hero */
.hero{position:absolute;left:0;top:138px;width:1024px;height:300px;background:linear-gradient(90deg,#b8c9cf 0,#dce8ea 30%,var(--mist) 55%,#c9d9dc 100%)}
.hero-worker{position:absolute;left:70px;top:0;width:300px;height:300px;background:linear-gradient(180deg,#e3c34a 0,#d8b07e 25%,#b94b40 55%,#8a5a34 100%);border-radius:140px 140px 0 0;opacity:.85}
.hero-band{position:absolute;left:0;top:210px;width:1024px;height:90px;background:linear-gradient(90deg,var(--blue-deep),var(--blue) 45%,var(--sky))}
.hero-title{left:314px;top:206px;font-weight:800;font-size:23px;color:var(--teal);letter-spacing:-.5px}
.hero-sub{left:314px;top:246px;font-weight:600;font-size:13px;line-height:20px;color:var(--blue)}
.hero-call{right:398px;top:364px;text-align:right;color:var(--white)}
.hero-call h3{font-weight:700;font-size:18px}
.hero-call p{font-weight:500;font-size:13.5px;line-height:17px}
.hero-call span{color:var(--mist);font-weight:800}

/* form */
.quote-card{position:absolute;left:646px;top:158px;width:248px;height:425px;background:var(--white);box-shadow:0 0 6px rgba(0,0,0,.4);padding:0 18px}
.quote-card h2{margin-top:18px;text-align:center;color:var(--blue);font-weight:700;font-size:18.5px}
.quote-card .intro{margin-top:8px;text-align:center;font-size:7.5px;line-height:14px;color:#555}
.quote-card .intro b{color:#333}
.field-label{display:block;font-size:8.5px;color:#444;margin-top:10px;margin-bottom:5px}
.field{height:26px;border:1px solid #cfcfcf;border-radius:2px;display:flex;align-items:center;padding-left:7px}
.field.focus{border-color:var(--sky);box-shadow:0 0 3px rgba(51,166,215,.5)}
.field .ico{width:14px;height:14px;border-right:1px solid #e2e2e2;padding-right:16px;box-sizing:content-box;display:flex}
.field.area{height:75px;align-items:flex-start;padding-top:6px}
.submit{margin-top:14px;height:33px;background:linear-gradient(var(--teal),var(--teal-deep));border-radius:2px;color:var(--white);font-weight:700;font-size:10.5px;display:flex;align-items:center;justify-content:center;box-shadow:0 2px 2px rgba(0,0,0,.3)}

/* content */
.section-title{position:absolute;left:138px;font-weight:700;font-size:18.5px;color:#a8a8a8}
.section-title span{color:var(--sky)}
.welcome-photo{left:138px;top:510px;width:112px;height:68px;background:linear-gradient(#a24b35 0,#8f3e2c 35%,#d9cfbf 36%,#c9bfad 85%,#eee 86%)}
.welcome-text{left:266px;top:507px;width:352px;font-size:10px;line-height:14.4px;color:#b4b4b4}
.welcome-text b{color:#d8d8d8}
.service{position:absolute;top:655px;width:108px;text-align:center}
.service .disc{width:108px;height:108px;border-radius:50%;background:radial-gradient(circle at 50% 30%,#5a5a5a,#3a3a3a 70%);box-shadow:0 3px 4px rgba(0,0,0,.6),inset 0 1px 0 #777;display:flex;align-items:center;justify-content:center}
.service p{margin-top:14px;font-size:13.5px;color:#b6b6b6;font-weight:500}
.testimonial{position:absolute;top:879px;width:236px}
.testimonial q{display:block;font-style:italic;font-weight:500;font-size:9.5px;line-height:16px;color:#a9a9a9;quotes:"“" "”"}
.testimonial .who{margin-top:18px;display:flex;align-items:center;gap:10px}
.testimonial .name{font-size:12px;color:#e6e6e6}
.testimonial .org{font-size:7.5px;color:#999;letter-spacing:.5px}

/* side promos */
.promo{position:absolute;left:651px;width:240px;height:109px;background:linear-gradient(135deg,var(--blue),var(--sky));box-shadow:0 2px 3px rgba(0,0,0,.5)}
.promo .portrait{position:absolute;left:0;bottom:0;width:86px;height:109px;background:linear-gradient(#2e86b8,#2c3a4c 60%,#23303f)}
.promo .copy{position:absolute;left:94px;top:18px}
.promo h4{font-weight:700;font-size:21px;line-height:26px;color:var(--white)}
.promo em{display:block;font-weight:500;font-size:13px;color:var(--mist);letter-spacing:.5px}
.promo small{display:block;margin-top:11px;font-weight:700;font-size:9.5px;line-height:13px;letter-spacing:.8px;color:#0b2f57}

/* footer */
.site-footer{position:absolute;left:0;top:1016px;width:1024px;height:160px;background:linear-gradient(#454545,#333)}
.foot-brand{left:127px;top:1028px;width:183px;height:80px;border:3px solid var(--blue);display:flex;align-items:center;justify-content:center;gap:7px}
.foot-brand .brand-name{color:#171717}
.foot-brand .brand-mark{background:var(--blue)}
.foot-head{position:absolute;top:1043px;font-size:12.5px;letter-spacing:1px;color:#8c8c8c;font-weight:500}
.foot-nav{left:333px;top:1069px;list-style:none;font-size:8.5px;line-height:19.2px;color:#e2e2e2}
.foot-nav li::before{content:"";display:inline-block;border-left:4px solid var(--sky);border-top:3px solid transparent;border-bottom:3px solid transparent;margin-right:7px}
.card{position:absolute;width:40px;height:25px;border-radius:3px;box-shadow:0 1px 2px rgba(0,0,0,.5)}
.contact-line{position:absolute;font-size:8.5px;line-height:14.4px;color:#bdbdbd;white-space:nowrap}
.contact-line b{color:#fff;font-weight:500}
.bottom-bar{position:absolute;left:0;top:1176px;width:1024px;height:24px;background:#262626;border-top:1px solid #1a1a1a;font-size:8.5px;color:#8a8a8a;line-height:24px}
</style>
</head>
<body>

<header class="site-header">
  <div class="brand"><span class="brand-mark"></span><span class="brand-name">Marlow Lift Gates</span></div>
  <p class="abs tagline">Family owned and<br>operated since 1965<span class="spanish">SE HABLA ESPAÑOL</span></p>
  <svg class="abs fish" width="34" height="16" viewBox="0 0 34 16" aria-hidden="true"><path d="M2 14 C10 -2 24 -2 32 8 C24 18 10 18 2 2" fill="none" stroke="#e6e6e6" stroke-width="1.8"/></svg>
  <p class="abs callout"><svg width="11" height="11" viewBox="0 0 11 11"><rect x=".5" y=".5" width="10" height="10" rx="1" fill="none" stroke="#999"/><path d="M3 3 l1.5 0 l.6 1.5 l-.8.6 a4 4 0 0 0 1.6 1.6 l.6-.8 l1.5.6 l0 1.5 a5 5 0 0 1 -5-5z" fill="#999"/></svg>CALL US NOW. <b>FREE</b> ESTIMATE!</p>
  <p class="abs head-phones">North County: <span>760.555.0142</span><br>South County: <span>619.555.0187</span></p>
  <div class="abs license">CA LICENSE #524906</div>
  <div class="abs quote-btn"><svg width="10" height="8" viewBox="0 0 10 8"><rect x=".5" y=".5" width="9" height="7" fill="none" stroke="#fff"/><path d="M.5 .5 L5 4.5 L9.5 .5" fill="none" stroke="#fff"/></svg>REQUEST A QUOTE</div>
</header>

<nav class="main-nav">
  <a class="active" style="left:264px;width:86px">HOME</a>
  <a style="left:350px;width:110px">ABOUT US</a>
  <a style="left:460px;width:174px">SERVICE/OPERATORS</a>
  <a style="left:634px;width:132px">GARAGE DOOR</a>
  <a style="left:766px;width:130px;border-right:1px solid #043f7a">STEEL SERVICES</a>
</nav>

<section class="hero">
  <div class="hero-band"></div>
  <div class="hero-worker" role="img" aria-label="Smiling technician in hard hat and plaid shirt holding a coiled cable, in front of a home with a garage door"></div>
</section>
<h1 class="abs hero-title">We repair all garage doors.</h1>
<p class="abs hero-sub">Installations for commercial and residential.<br>No job is too big or too small.</p>
<div class="abs hero-call">
  <h3>Call now for FREE estimate!</h3>
  <p>North County: <span>760.555.0142</span></p>
  <p>South County: <span>619.555.0187</span></p>
</div>

<aside class="quote-card">
  <h2>REQUEST A QUOTE</h2>
  <p class="intro">We have <b>spanish</b> speakers on site, we accept all <b>major credit cards</b>, we have senior and military <b>discounts.</b></p>
  <span class="field-label" style="margin-top:20px">Your Name</span>
  <div class="field focus"><span class="ico"><svg width="14" height="14" viewBox="0 0 14 14"><circle cx="7" cy="4.5" r="3" fill="#ccc"/><path d="M1.5 14 a5.5 5 0 0 1 11 0z" fill="#ccc"/></svg></span></div>
  <span class="field-label">Your Phone Number</span>
  <div class="field"><span class="ico"><svg width="14" height="14" viewBox="0 0 14 14"><path d="M1 5 a6 3 0 0 1 12 0 l0 1.5 l-3 0 l0-1.5 l-6 0 l0 1.5 l-3 0z M3 7 l8 0 l1.5 6 l-11 0z" fill="#ccc"/></svg></span></div>
  <span class="field-label">Your Email Address</span>
  <div class="field"><span class="ico"><svg width="14" height="14" viewBox="0 0 14 14"><rect x="1" y="3" width="12" height="8" fill="#ccc"/><path d="M1 3 L7 8 L13 3" fill="none" stroke="#fff"/></svg></span></div>
  <span class="field-label">Your Message</span>
  <div class="field area"><span class="ico"><svg width="14" height="14" viewBox="0 0 14 14"><circle cx="8" cy="2.5" r="1.5" fill="#ccc"/><path d="M6 6 l3 0 l-1.5 7 l-2 0z" fill="#ccc"/></svg></span></div>
  <div class="submit">SUBMIT YOUR MESSAGE</div>
</aside>

<h2 class="section-title" style="top:466px">Welcome to <span>Marlow Lift Gates</span></h2>
<div class="abs welcome-photo" role="img" aria-label="Brick house with a closed white sectional garage door"></div>
<p class="abs welcome-text">How many times have you had to open your garage door by hand and wondered, <b>“There has got to be an easier way,”</b> How many times have you thought to yourself, “The neighbor’s garage door is so much easier to handle and looks nicer than ours. I wish we had a door like that?” If you have been in either of these predicaments, it’s time you do something about it!</p>

<h2 class="section-title" style="top:612px">Our <span>Services</span></h2>
<div class="service" style="left:139px"><div class="disc"><svg width="60" height="50" viewBox="0 0 60 50"><path d="M4 18 L30 4 L56 18" fill="none" stroke="#fff" stroke-width="5" stroke-linejoin="round"/><rect x="13" y="20" width="34" height="26" fill="none" stroke="#fff" stroke-width="4"/><path d="M15 29 H45 M15 36 H45 M15 42 H45" stroke="#fff" stroke-width="3"/><rect x="25" y="10" width="10" height="7" fill="none" stroke="#fff" stroke-width="2"/></svg></div><p>INSTALLATION</p></div>
<div class="service" style="left:267px"><div class="disc"><svg width="54" height="54" viewBox="0 0 54 54"><path d="M8 6 l10 0 l5 12 l-6 5 a26 26 0 0 0 14 14 l5-6 l12 5 l0 10 a8 8 0 0 1-8 8 C20 52 2 34 2 14 a8 8 0 0 1 6-8z" fill="#fff"/><path d="M30 24 L44 10" stroke="#fff" stroke-width="6" stroke-linecap="round"/><circle cx="46" cy="8" r="6" fill="none" stroke="#fff" stroke-width="4"/></svg></div><p>SERVICE</p></div>
<div class="service" style="left:395px"><div class="disc"><svg width="60" height="56" viewBox="0 0 60 56"><path d="M6 10 a8 8 0 0 1 8-8 l24 4 l0 16 l-24 4 a8 8 0 0 1-8-8z" fill="#fff"/><rect x="38" y="10" width="8" height="8" fill="#fff"/><path d="M46 14 L58 12" stroke="#fff" stroke-width="2" stroke-dasharray="2 1"/><path d="M18 24 l10 0 l-2 20 l-8 0z" fill="#fff"/><path d="M24 44 c0 10 14 10 14 0" fill="none" stroke="#fff" stroke-width="2"/></svg></div><p>REPAIRS</p></div>
<div class="service" style="left:523px"><div class="disc"><svg width="54" height="54" viewBox="0 0 54 54"><rect x="2" y="32" width="12" height="20" fill="#fff"/><rect x="20" y="18" width="12" height="34" fill="#fff"/><rect x="38" y="2" width="14" height="50" fill="#fff"/></svg></div><p>SALES</p></div>

<h2 class="section-title" style="top:834px">Client <span>Testimonials</span></h2>
<div class="testimonial" style="left:137px">
  <q>Lorem ipsum dolor sit amet, consectetur adipisicing elit, sed do eiusmod tempor incididunt eiusmod ut labore et dolore eiusmod magna.</q>
  <div class="who"><svg width="24" height="24" viewBox="0 0 24 24"><circle cx="12" cy="8" r="5.5" fill="#4a4a4a"/><path d="M1 24 a11 10 0 0 1 22 0z" fill="#4a4a4a"/></svg><div><div class="name">Daniel Reyes</div><div class="org">OAK STREET REALTY</div></div></div>
</div>
<div class="testimonial" style="left:392px">
  <q>Lorem ipsum dolor sit amet, consectetur adipisicing elit, sed do eiusmod tempor incididunt eiusmod ut labore et dolore eiusmod magna.</q>
  <div class="who"><svg width="24" height="24" viewBox="0 0 24 24"><circle cx="12" cy="8" r="5.5" fill="#4a4a4a"/><path d="M1 24 a11 10 0 0 1 22 0z" fill="#4a4a4a"/></svg><div><div class="name">Daniel Reyes</div><div class="org">OAK STREET REALTY</div></div></div>
</div>

<div class="promo" style="top:610px"><div class="portrait" role="img" aria-label="Woman technician in hard hat and work jacket"></div><div class="copy"><h4>45 YEARS</h4><em>of experience.</em><small>GUARANTEED QUALITY<br>SERVICE</small></div></div>
<div class="promo" style="top:739px"><div class="portrait" role="img" aria-label="Senior man with glasses in a plaid shirt"></div><div class="copy"><h4>DISCOUNTS</h4><em>&amp; exclusive offers</em><small>SENIOR AND MILITARY<br>DISCOUNTS OFFERED.</small></div></div>
<div class="promo" style="top:870px"><div class="portrait" role="img" aria-label="Young technician in hard hat and work shirt"></div><div class="copy" style="top:12px"><h4>SE HABLA<br>ESPAÑOL</h4><small style="margin-top:8px">SPANISH SPEAKERS ON<br>SITE TO ASSIST YOU.</small></div></div>

<footer class="site-footer"></footer>
<div class="abs foot-brand"><span class="brand-mark"></span><span class="brand-name">Marlow Lift Gates</span></div>
<h5 class="foot-head" style="left:329px">NAVIGATION</h5>
<ul class="abs foot-nav"><li>About</li><li>Services/Operators</li><li>Garage Door</li><li>Contact</li></ul>
<h5 class="foot-head" style="left:458px">WE ACCEPT:</h5>
<div class="card" style="left:458px;top:1077px;background:#f4f4f4"></div>
<div class="card" style="left:507px;top:1077px;background:#f3e7b8"></div>
<div class="card" style="left:559px;top:1077px;background:#f4f4f4"></div>
<div class="card" style="left:458px;top:1113px;background:#1d5fb0"></div>
<div class="card" style="left:507px;top:1113px;background:#2a4fa0"></div>
<div class="card" style="left:559px;top:1113px;background:#2f86c9"></div>
<h5 class="foot-head" style="left:633px">CONTACT</h5>
<svg class="abs" style="left:633px;top:1076px" width="15" height="11" viewBox="0 0 15 11"><rect width="15" height="11" fill="#8a8a8a"/><path d="M0 0 L7.5 6 L15 0" fill="none" stroke="#444"/></svg>
<p class="contact-line" style="left:654px;top:1072px">North County: <b>marlowgates@mailbox.com</b><br>South County: <b>marlowgates619@mailbox.com</b></p>
<svg class="abs" style="left:634px;top:1118px" width="11" height="15" viewBox="0 0 11 15"><path d="M5.5 15 C1 9 0 7 0 5.5 a5.5 5.5 0 0 1 11 0 C11 7 10 9 5.5 15z" fill="#8a8a8a"/><circle cx="5.5" cy="5.5" r="2" fill="#3a3a3a"/></svg>
<p class="contact-line" style="left:654px;top:1115px"><b>4815 Cedar Ridge Pl</b><br><b>Vista, CA 92084</b></p>
<svg class="abs" style="left:760px;top:1118px" width="13" height="13" viewBox="0 0 13 13"><path d="M2 0 l3 0 l1 3 l-1.5 1.5 a7 7 0 0 0 4 4 l1.5-1.5 l3 1 l0 3 a2 2 0 0 1-2 2 C5 13 0 8 0 2 a2 2 0 0 1 2-2z" fill="#8a8a8a"/></svg>
<p class="contact-line" style="left:783px;top:1115px">North County: <b>760.555.0142</b><br>South County: <b>619.555.0187</b></p>

<div class="bottom-bar">
  <span class="abs" style="left:132px">Copyright 2014 © Marlow Lift Gates - All Rights Reserved</span>
  <span class="abs" style="left:635px">Site Map &nbsp; • &nbsp; Privacy Policy &nbsp; • &nbsp; Disclaimer</span>
</div>

</body>
</html>
```